goal design

We are rolling out a goal for the next 3 years. the goal is as follows:
2014: $8 million gross profit, $1.25 million net income
2015: $12 million gross profit, $2.4 million net income
2016 $15 million gross profit, $4 million net income
We want a design that captures these numbers and that we can publish company wide that will quickly remind everyone of these goals. Our website is www.brookvalerecruiting.example. This will be an internal campaign. We will use the simple design to remind our people of our goals for the next 3 years. We will print it on mouse pads, shirts and things of this nature periodically to keep it front of mind for our people. So easy to remember, visually appealing and simple are good guidelines.
Updates
Target Market(s)
This is an internal campaign. it is to remind our people of our goals for the next few years so will be on little reminder items (i.e. cell phone covers, mouse pads, shirts, screen savers, etc).
Industry/Entity Type
It Company
Look and feel

```html
<!DOCTYPE html>
<html lang="en">
<head>
<meta charset="utf-8">
<title>Three-Year Goals – Brookvale Recruiting</title>
<link href="https://fonts.googleapis.com/css2?family=Jost:wght@300;400;600;700;800&display=swap" rel="stylesheet">
<style>
  :root {
    --navy: #0d3a66;
    --navy-soft: rgba(13, 58, 102, 0.16);
    --sky-edge: #b9c6dc;
    --sky-mid: #e4e9f2;
    --white: #ffffff;
  }
  * { margin: 0; padding: 0; box-sizing: border-box; }
  html, body { width: 1075px; height: 1200px; overflow: hidden; }
  body {
    font-family: "Jost", sans-serif;
    color: var(--navy);
    background: radial-gradient(ellipse 70% 60% at 50% 62%, var(--white) 0%, var(--sky-mid) 60%, var(--sky-edge) 100%);
    position: relative;
  }
  .ridge-art {
    position: absolute; top: 0; left: 0; width: 1075px; height: 235px;
    background: linear-gradient(180deg, var(--navy-soft) 0%, rgba(13, 58, 102, 0.06) 70%, rgba(13, 58, 102, 0) 100%);
  }
  .headline {
    position: absolute; top: 268px; left: 0; width: 100%;
    text-align: center; font-size: 72px; line-height: 86px; font-weight: 400;
  }
  .headline strong { display: block; font-weight: 700; font-size: 70px; }
  .goals { position: absolute; top: 550px; left: 122px; }
  .goal-row { display: flex; align-items: center; height: 124px; }
  .goal-year {
    font-size: 140px; line-height: 1; font-weight: 400; letter-spacing: -2px;
    width: 332px;
  }
  .goal-year b { font-weight: 800; }
  .goal-figures { font-size: 44px; line-height: 48px; font-weight: 300; white-space: nowrap; }
  .goal-figures b { font-weight: 700; }
  .brand {
    position: absolute; top: 1020px; left: 0; width: 100%;
    display: flex; justify-content: center; align-items: center; gap: 14px;
  }
  .brand-dot { width: 22px; height: 22px; border-radius: 50%; background: var(--navy); }
  .brand-name {
    font-size: 34px; font-weight: 600; letter-spacing: 3px; text-transform: uppercase;
    color: var(--navy);
  }
</style>
</head>
<body>
  <div class="ridge-art" role="img" aria-label="Mountain ridge line illustration across the top"></div>

  <h1 class="headline">Our sense of urgency and<br>personalized solutions<strong>will set us apart</strong></h1>

  <section class="goals">
    <div class="goal-row">
      <div class="goal-year">20<b>14</b></div>
      <div class="goal-figures"><b>$8 million</b> gross profit<br><b>$1.25 million</b> net income</div>
    </div>
    <div class="goal-row">
      <div class="goal-year">20<b>15</b></div>
      <div class="goal-figures"><b>$12 million</b> gross profit<br><b>$2.4 million</b> net income</div>
    </div>
    <div class="goal-row">
      <div class="goal-year">20<b>16</b></div>
      <div class="goal-figures"><b>$15 million</b> gross profit<br><b>$4 million</b> net income</div>
    </div>
  </section>

  <footer class="brand">
    <span class="brand-dot"></span>
    <span class="brand-name">Brookvale Recruiting</span>
  </footer>
</body>
</html>
```